Marrowfield Contracting Business Cards

Front of card:

Full Logo
Name
Address
Office Phone
Cell Phone
Email
Website

Back:
Logo Mark in background
List and markets and services performed

```html
<!DOCTYPE html>
<html lang="en">
<head>
<meta charset="utf-8">
<title>Marrowfield Contracting Business Cards</title>
<link href="https://fonts.googleapis.com/css2?family=Exo+2:wght@400;500;600;700&display=swap" rel="stylesheet">
<style>
  :root {
    --page: #ffffff;
    --brand-red: #d01b1b;
    --ink-grey: #6d6e70;
    --card-white: #ffffff;
    --text-light: #ffffff;
    --shadow: 0 14px 30px rgba(0,0,0,0.28);
  }
  * { margin: 0; padding: 0; box-sizing: border-box; }
  html, body {
    width: 1200px; height: 1200px; overflow: hidden;
    background: var(--page);
    font-family: "Exo 2", sans-serif;
  }
  .sheet {
    width: 1200px; height: 1200px;
    display: flex; flex-direction: column; align-items: center; justify-content: center;
    gap: 64px;
  }
  .card {
    position: relative;
    width: 880px; height: 508px;
    box-shadow: var(--shadow);
  }
  .card--front { background: var(--brand-red); color: var(--text-light); }
  .card--back { background: var(--card-white); }

  .wordmark { display: flex; align-items: center; gap: 14px; }
  .wordmark__dot { border-radius: 50%; flex: none; }
  .wordmark__name {
    font-weight: 700; text-transform: uppercase; line-height: 1.05;
    letter-spacing: 0.04em;
  }
  .wordmark__llc { display: block; text-align: right; font-size: 0.55em; letter-spacing: 0.2em; }

  .card--front .wordmark { position: absolute; top: 78px; right: 48px; }
  .card--front .wordmark__dot { width: 62px; height: 62px; border: 6px solid var(--text-light); }
  .card--front .wordmark__name { font-size: 26px; color: var(--text-light); }

  .holder { position: absolute; left: 48px; top: 272px; }
  .holder__name { font-size: 46px; font-weight: 500; letter-spacing: 0.02em; line-height: 1; }
  .holder__title { font-size: 18px; font-weight: 400; margin-top: 8px; }

  .contacts {
    position: absolute; left: 48px; right: 40px; top: 392px;
    display: flex; align-items: stretch;
    font-size: 17px; font-weight: 500;
  }
  .contacts__group { display: flex; flex-direction: column; gap: 8px; padding: 0 26px; border-left: 1.5px solid rgba(255,255,255,0.7); }
  .contacts__group:first-child { padding-left: 0; border-left: none; }
  .contacts__row { display: flex; align-items: flex-start; gap: 10px; white-space: nowrap; }
  .contacts__row--plain { padding-left: 30px; }
  .icon { width: 20px; height: 20px; flex: none; margin-top: 1px; }

  .card--back .wordmark { position: absolute; top: 150px; left: 50%; transform: translateX(-50%); flex-direction: column; gap: 18px; }
  .card--back .wordmark__dot { width: 110px; height: 110px; background: var(--brand-red); }
  .card--back .wordmark__name { font-size: 40px; color: var(--ink-grey); text-align: center; }

  .services {
    position: absolute; left: 44px; right: 44px; top: 446px;
    display: flex; align-items: center; gap: 14px;
  }
  .services__rule { flex: 1; height: 2px; background: var(--brand-red); }
  .services__text { color: var(--brand-red); font-size: 17px; font-weight: 500; white-space: nowrap; }
</style>
</head>
<body>
<main class="sheet">
  <section class="card card--front" aria-label="Card front">
    <div class="wordmark">
      <span class="wordmark__dot"></span>
      <span class="wordmark__name">Marrowfield<br>Contracting<span class="wordmark__llc">LLC</span></span>
    </div>
    <div class="holder">
      <p class="holder__name">John Smith</p>
      <p class="holder__title">Managing Director</p>
    </div>
    <div class="contacts">
      <div class="contacts__group">
        <div class="contacts__row">
          <svg class="icon" viewBox="0 0 20 20"><circle cx="10" cy="10" r="10" fill="#fff"/><path d="M7 5.5l2 2-1 1.3c.7 1.4 1.8 2.5 3.2 3.2l1.3-1 2 2-1.2 1.5c-3.8-.6-7-3.8-7.6-7.6z" fill="#d01b1b"/></svg>
          <span>(000)123-4567</span>
        </div>
        <div class="contacts__row contacts__row--plain"><span>(000)234-5765</span></div>
      </div>
      <div class="contacts__group">
        <div class="contacts__row">
          <svg class="icon" viewBox="0 0 20 20"><circle cx="10" cy="10" r="10" fill="#fff"/><circle cx="10" cy="10" r="3" fill="none" stroke="#d01b1b" stroke-width="1.6"/><path d="M13 10v1.2c0 1.2 2 1.2 2 0V10a5 5 0 1 0-2 4" fill="none" stroke="#d01b1b" stroke-width="1.6"/></svg>
          <span>yourgmail@name.com</span>
        </div>
        <div class="contacts__row">
          <svg class="icon" viewBox="0 0 20 20"><circle cx="10" cy="10" r="10" fill="#fff"/><circle cx="10" cy="10" r="5.5" fill="none" stroke="#d01b1b" stroke-width="1.3"/><path d="M4.5 10h11M10 4.5c-2.5 3-2.5 8 0 11M10 4.5c2.5 3 2.5 8 0 11" fill="none" stroke="#d01b1b" stroke-width="1.2"/></svg>
          <span>www.websitename.com</span>
        </div>
      </div>
      <div class="contacts__group">
        <div class="contacts__row">
          <svg class="icon" viewBox="0 0 20 20"><circle cx="10" cy="10" r="10" fill="#fff"/><path d="M10 4a4 4 0 0 0-4 4c0 3 4 7.5 4 7.5s4-4.5 4-7.5a4 4 0 0 0-4-4z" fill="#d01b1b"/><circle cx="10" cy="8" r="1.5" fill="#fff"/></svg>
          <span>123 Street Name City Name<br>State, Country, 12345</span>
        </div>
      </div>
    </div>
  </section>

  <section class="card card--back" aria-label="Card back">
    <div class="wordmark">
      <span class="wordmark__dot"></span>
      <span class="wordmark__name">Marrowfield<br>Contracting<span class="wordmark__llc">LLC</span></span>
    </div>
    <div class="services">
      <span class="services__rule"></span>
      <span class="services__text">List and Markets and Services Performed</span>
    </div>
  </section>
</main>
</body>
</html>
```